Business Card Design for new logo

Business card Design for new logo. Follow colors from logo.
The company has offices in multiple comtries
Want to have some bulltes on the countries and also on the main services

Something like
USA*Dominican Republic*LATAM

Consulting*Healthcare IT*Tranformation

Industry/Entity Type

Information Technology

Contact Information for Business Card

Address, Phones, countries, name and position

Miron castell

Founder and CEO

947 Quarry Ln
Mill haven, PA 16835

Mcastell@novelquin.com

www.novelquin.com

717-352-6081

828-444-4444

```html
<!DOCTYPE html>
<html lang="en">
<head>
<meta charset="utf-8">
<title>Novelquin Health – Business Card</title>
<link rel="stylesheet" href="https://fonts.googleapis.com/css2?family=Open+Sans:wght@400;600&display=swap">
<style>
  :root {
    --backdrop: #393939;
    --brand-blue: #2774b5;
    --brand-orange: #f48c51;
    --card-white: #ffffff;
    --ink: #444444;
    --divider: #d6d6d6;
  }
  * { margin: 0; padding: 0; box-sizing: border-box; }
  html, body {
    width: 1200px; height: 900px; overflow: hidden;
    background: var(--backdrop);
    font-family: "Open Sans", Arial, sans-serif;
  }
  .stage { position: relative; width: 1200px; height: 900px; }

  .card {
    position: absolute;
    width: 477px; height: 293px;
    overflow: hidden;
    box-shadow: 3px 4px 6px rgba(0,0,0,0.55);
  }
  .card-front {
    left: 120px; top: 275px;
    background: var(--card-white);
    border-radius: 0 46px 0 46px;
  }
  .card-back {
    left: 606px; top: 274px;
    background: var(--brand-blue);
    border-radius: 46px 0 46px 0;
  }

  .band {
    position: absolute; left: 0; right: 0; bottom: 0; height: 50px;
    display: flex; align-items: center; justify-content: center;
    gap: 12px;
    color: #fff; font-size: 14.5px;
  }
  .band-services { background: var(--brand-blue); padding-left: 14px; }
  .band-countries { background: var(--brand-orange); }
  .band .dot {
    width: 8px; height: 8px; border-radius: 50%; background: #fff;
    margin: 0 6px;
  }

  .brand-lockup {
    position: absolute; left: 28px; top: 168px; width: 220px;
    text-align: center;
    color: var(--brand-blue); font-size: 25px; font-weight: 600;
    letter-spacing: 0.2px;
  }
  .brand-mark {
    position: absolute; left: 118px; top: 100px;
    width: 44px; height: 44px; border-radius: 50%;
    background: var(--brand-orange);
  }

  .divider {
    position: absolute; left: 246px; top: 53px;
    width: 1px; height: 182px; background: var(--divider);
  }

  .contact { position: absolute; left: 264px; top: 67px; color: var(--ink); }
  .contact-name { color: var(--brand-blue); font-size: 20px; font-weight: 600; line-height: 26px; }
  .contact-title { font-size: 14px; line-height: 18px; }
  .contact-address { margin-top: 6px; font-size: 14px; line-height: 17px; }
  .contact-lines { margin-top: 7px; list-style: none; font-size: 14px; line-height: 17.5px; }
  .contact-lines li { display: flex; align-items: center; gap: 5px; }
  .contact-lines svg { width: 11px; height: 11px; fill: var(--brand-blue); flex: none; }

  .back-lockup {
    position: absolute; left: 0; right: 0; top: 80px;
    display: flex; flex-direction: column; align-items: center; gap: 18px;
    color: #fff; font-size: 26px; font-weight: 600;
  }
  .back-lockup .brand-mark-large {
    width: 70px; height: 70px; border-radius: 50%; background: #fff;
  }
</style>
</head>
<body>
<main class="stage">

  <section class="card card-front">
    <span class="brand-mark" aria-hidden="true"></span>
    <div class="brand-lockup">Novelquin Health</div>
    <div class="divider"></div>

    <div class="contact">
      <div class="contact-name">Miron Castell</div>
      <div class="contact-title">Founder and CEO</div>
      <div class="contact-address">947 Quarry Ln<br>Mill haven, PA 16835</div>
      <ul class="contact-lines">
        <li><svg viewBox="0 0 12 12" aria-hidden="true"><path d="M1 5c0-2 2-3 5-3s5 1 5 3l-2 1-1-2H4L3 6zM3 7h6l1 4H2z"/></svg>717-352-6081</li>
        <li><svg viewBox="0 0 12 12" aria-hidden="true"><path d="M3 0h6v12H3zM4 1.5v8h4v-8z"/></svg>828-444-4444</li>
        <li><svg viewBox="0 0 12 12" aria-hidden="true"><path d="M0 2h12v8H0zM1 3l5 4 5-4v-.2H1z"/></svg>Mcastell@novelquin.com</li>
        <li><svg viewBox="0 0 12 12" aria-hidden="true"><circle cx="6" cy="6" r="5.5"/></svg>www.novelquin.com</li>
      </ul>
    </div>

    <div class="band band-services">
      <span>Consulting</span><span class="dot"></span>
      <span>Healthcare IT</span><span class="dot"></span>
      <span>Tranformation</span>
    </div>
  </section>

  <section class="card card-back">
    <div class="back-lockup">
      <span class="brand-mark-large" aria-hidden="true"></span>
      <span>Novelquin Health</span>
    </div>
    <div class="band band-countries">
      <span>USA</span><span class="dot"></span>
      <span>Dominican Republic</span><span class="dot"></span>
      <span>LATAM</span>
    </div>
  </section>

</main>
</body>
</html>
```